Tarvel Ridge LLC

Need Professional Business cards for New Investment Fund

Target Market(s)

High Quality investors

Industry/Entity Type

Financial

Contact Information for Business Card

Phone Number +1 555 284 6193
Name Pavel Orlinsky
Title Fund Manager
email po@FundTarvel.example
Website www.FundTarvel.example

Colors

Designer to choose colors to be used in the design.

Requirements
Must have
• Must have our Logo and all of the above. Must be made so lettering and loge can be raised

```html
<!DOCTYPE html>
<html lang="en">
<head>
<meta charset="utf-8">
<title>Tarvel Ridge LLC – Business Card</title>
<link rel="stylesheet" href="https://fonts.googleapis.com/css2?family=Arimo&family=Jost:wght@500&display=swap">
<style>
  :root {
    --page: #ffffff;
    --card-black: #060708;
    --brand-yellow: #f2ec31;
    --brand-green: #8cc63f;
    --text-white: #ffffff;
    --card-shadow: rgba(0, 0, 0, 0.35);
  }
  * { margin: 0; padding: 0; box-sizing: border-box; }
  html, body { width: 919px; height: 1200px; overflow: hidden; background: var(--page); }
  body { position: relative; font-family: "Arimo", Arial, sans-serif; }

  .card {
    position: absolute;
    left: 183px;
    width: 554px;
    height: 317px;
    border-radius: 10px;
    background: var(--card-black);
    overflow: hidden;
    box-shadow: 4px 6px 8px var(--card-shadow);
  }
  .card--front { top: 249px; }
  .card--back { top: 648px; }

  .front-waves { position: absolute; inset: 0; width: 554px; height: 317px; }

  .brand { position: absolute; display: flex; align-items: center; gap: 10px; }
  .brand__mark { width: 16px; height: 16px; background: var(--brand-green); }
  .brand__name {
    font-family: "Jost", "Futura", sans-serif;
    font-weight: 500;
    color: var(--brand-green);
    letter-spacing: 0.3px;
    white-space: nowrap;
  }
  .card--front .brand { left: 36px; top: 63px; }
  .card--front .brand__name { font-size: 23px; }
  .card--back .brand { left: 0; right: 0; top: 204px; justify-content: center; }
  .card--back .brand__name { font-size: 27px; }
  .card--back .brand__mark { width: 20px; height: 20px; }

  .holder { position: absolute; left: 315px; top: 147px; }
  .holder__name { color: var(--brand-green); font-size: 19px; letter-spacing: 0.4px; line-height: 24px; }
  .holder__title { color: var(--text-white); font-size: 14px; line-height: 18px; }

  .contacts { position: absolute; left: 316px; top: 207px; list-style: none; }
  .contacts__item {
    display: flex; align-items: center; gap: 13px;
    height: 33px; color: var(--text-white); font-size: 14px; letter-spacing: 0.4px;
  }
  .contacts__icon { width: 19px; height: 19px; flex: none; }

  .address {
    position: absolute; left: 34px; top: 249px;
    color: var(--text-white); font-size: 14px; line-height: 22px; text-align: center;
    font-style: normal;
  }
</style>
</head>
<body>

<section class="card card--front" aria-label="Business card front">
  <svg class="front-waves" viewBox="0 0 554 317" aria-hidden="true">
    <path fill="var(--brand-yellow)" d="M0,0 H540 C430,92 250,152 0,161 Z"/>
    <path fill="var(--brand-green)" d="M0,185 C160,182 300,160 430,116 C310,170 160,199 0,201 Z"/>
    <path fill="var(--brand-yellow)" d="M0,203 C210,199 420,138 542,2 L550,4 C430,150 210,210 0,209 Z"/>
  </svg>

  <div class="brand">
    <span class="brand__mark"></span>
    <span class="brand__name">TARVEL RIDGE LLC</span>
  </div>

  <div class="holder">
    <p class="holder__name">Pavel Orlinsky</p>
    <p class="holder__title">Fund Manager</p>
  </div>

  <ul class="contacts">
    <li class="contacts__item">
      <svg class="contacts__icon" viewBox="0 0 20 20" aria-hidden="true">
        <path fill="var(--brand-green)" d="M4.5,1.5 L7.5,1 L9,5.5 L6.8,7.2 C7.8,9.6 9.8,11.8 12.5,13 L14.2,11 L18.7,12.5 L18.2,16 C17.8,17.8 16,18.7 14,18 C8.5,16.2 3.8,11.5 2,6 C1.4,4 2.5,2 4.5,1.5 Z"/>
      </svg>
      <span>+1 555 284 6193</span>
    </li>
    <li class="contacts__item">
      <svg class="contacts__icon" viewBox="0 0 20 20" aria-hidden="true">
        <rect x="1" y="4" width="18" height="12" fill="var(--brand-green)"/>
        <path d="M1,4 L10,11 L19,4 M1,16 L7.5,9 M19,16 L12.5,9" fill="none" stroke="var(--card-black)" stroke-width="1"/>
      </svg>
      <span>po@FundTarvel.example</span>
    </li>
    <li class="contacts__item">
      <svg class="contacts__icon" viewBox="0 0 20 20" aria-hidden="true">
        <circle cx="10" cy="10" r="9.5" fill="var(--brand-green)"/>
        <g fill="none" stroke="var(--card-black)" stroke-width="0.9">
          <ellipse cx="10" cy="10" rx="4" ry="9.5"/>
          <path d="M0.5,10 H19.5 M2,5.5 H18 M2,14.5 H18 M10,0.5 V19.5"/>
        </g>
      </svg>
      <span>www.FundTarvel.example</span>
    </li>
  </ul>

  <address class="address">address line1<br>address line 2</address>
</section>

<section class="card card--back" aria-label="Business card back">
  <div class="brand">
    <span class="brand__mark"></span>
    <span class="brand__name">TARVEL RIDGE LLC</span>
  </div>
</section>

</body>
</html>
```